Commercial painting company is looking for a creative website designer.

Hi, we just completed our logo project and now ready to launch our website. The project will be done on Squarespace platform. It will contain:
Page 1 HOME
Page 2 SERVICES
Page 3 PICTURES
The content will be written by us. I am not sure bout the pictures, I do not have any to provide. I can buy stock photos if needed.
We are commercial only painting company and have to appeal to commercial, industrial property mangers. We will need CALL, REQUEST FOR ESTIMATE buttons.
If possible to have a live picture on home page would be great. Thank you
Target Market(s)
Property Managers
Industry/Entity Type
Commercial Painting
Other font styles liked:
- Poppins

```html
<!DOCTYPE html>
<html lang="en">
<head>
<meta charset="utf-8">
<title>Brushline Coatings — Commercial Painting</title>
<link rel="stylesheet" href="https://fonts.googleapis.com/css2?family=Rubik:wght@400;500;600&family=Roboto:wght@400;500&display=swap">
<style>
:root{
  --navy:#06276b;
  --red:#c60f2e;
  --text:#7b7f86;
  --ink:#2b2f36;
  --field:#f6f6f6;
  --field-line:#e2e2e2;
  --footer:#ececec;
  --white:#ffffff;
}
*{box-sizing:border-box;margin:0;padding:0}
html,body{width:1200px;height:4082px;overflow:hidden;background:var(--white)}
body{position:relative;font-family:"Roboto",Arial,sans-serif;color:var(--text)}
.abs{position:absolute}
.heading{font-family:"Rubik",Arial,sans-serif;font-weight:500;color:var(--navy);text-transform:uppercase}
.btn{position:absolute;display:flex;align-items:center;justify-content:center;background:var(--red);color:var(--white);font-family:"Rubik",Arial,sans-serif;font-weight:500;font-size:14px;text-transform:uppercase;letter-spacing:.2px}
.copy{font-size:14.5px;line-height:26px;text-align:justify}

/* hero */
.hero{left:0;top:0;width:1200px;height:600px;background:linear-gradient(90deg,#e6e2d6 0%,#d8d3c4 35%,#b7b3a7 60%,#8f918d 75%,#9c9d98 100%)}
.hero::after{content:"";position:absolute;left:0;bottom:0;width:720px;height:130px;background:linear-gradient(180deg,rgba(190,180,160,0) 0%,#a69c88 100%)}
.brand{left:111px;top:20px;display:flex;align-items:center;gap:12px;z-index:2}
.brand-dot{width:22px;height:22px;border-radius:50%;background:var(--navy)}
.brand-name{font-family:"Rubik",Arial,sans-serif;font-weight:500;font-size:20px;color:var(--navy);line-height:94px}
.nav{left:416px;top:58px;display:flex;gap:26px;z-index:2}
.nav a{font-family:"Rubik",Arial,sans-serif;font-weight:500;font-size:13px;color:var(--ink);text-decoration:none;text-transform:uppercase}
.nav a.active{color:var(--red)}
.hero-title{left:111px;top:384px;font-size:35px;line-height:48px;letter-spacing:.8px;z-index:2}

/* about */
.about-title{left:111px;top:683px;font-size:52px;letter-spacing:1px}

/* services */
.services{left:0;top:1046px;width:1200px;height:1488px;background:var(--navy)}
.service-photo{position:absolute;width:489px;height:377px}
.service-title{position:absolute;color:var(--white);font-family:"Rubik",Arial,sans-serif;font-weight:500;font-size:27px;line-height:36px;text-transform:uppercase}
.service-copy{position:absolute;width:432px;color:var(--white);font-size:14.5px;line-height:26px;text-align:justify}

/* quote */
.quote{left:111px;top:2608px;width:900px;font-family:"Rubik",Arial,sans-serif;font-size:28.5px;line-height:43px;color:var(--navy)}
.quote-name{left:111px;top:2757px;font-family:"Rubik",Arial,sans-serif;font-weight:500;font-size:24px;color:var(--red)}
.wide-photo{left:0;top:2857px;width:1200px;height:433px;background:linear-gradient(120deg,#5cb6e0 0%,#dfe6ea 30%,#d9d9d9 45%,#c9413f 58%,#e4e4e4 72%,#3aa3d6 100%)}

/* contact */
.contact-title{left:111px;top:3377px;font-size:35px}
.label{font-family:"Rubik",Arial,sans-serif;font-weight:500;font-size:16px;color:var(--ink)}
.detail{font-size:15px;color:var(--text)}
.form-label{font-size:12.5px;color:var(--ink)}
.field{position:absolute;background:var(--field);border:1px solid var(--field-line);font-size:12px;color:#9a9da3;padding-left:16px;display:flex;align-items:center}

/* footer */
.footer{left:0;top:3815px;width:1200px;height:267px;background:var(--footer)}
.footer-head{font-family:"Rubik",Arial,sans-serif;font-weight:500;font-size:16px;color:var(--ink)}
.footer-link{font-size:14px;color:var(--ink);line-height:29px}
</style>
</head>
<body>

<header>
  <div class="abs hero" role="img" aria-label="Rope-access painter on a building facade above a city skyline"></div>
  <div class="abs brand"><span class="brand-dot"></span><span class="brand-name">Brushline Coatings</span></div>
  <nav class="abs nav">
    <a class="active" href="#">Home</a><a href="#">About Us</a><a href="#">Services</a><a href="#">Gallery</a><a href="#">Contact Us</a>
  </nav>
  <a class="btn" style="left:883px;top:41px;width:206px;height:50px;z-index:2">Request for Estimate</a>
  <h1 class="abs heading hero-title">Welcome to<br>Brushline Coatings</h1>
</header>

<section>
  <h2 class="abs heading about-title">About Us</h2>
  <p class="abs copy" style="left:111px;top:770px;width:488px">Lorem ipsum dolor sit amet, consectetur adipiscing elit, sed do eiusmod tempor incididunt ut labore et dolore magna aliqua. Ut enim ad minim veniam, quis nostrud exercitation ullamco laboris nisi ut aliquip ex ea commodo consequat.</p>
  <a class="btn" style="left:111px;top:907px;width:138px;height:50px">Call Us Now</a>
  <p class="abs copy" style="left:685px;top:689px;width:404px">Lorem ipsum dolor sit amet, consectetur adipiscing elit, sed do eiusmod tempor incididunt ut labore et dolore magna aliqua. Ut enim ad minim veniam, quis nostrud exercitation ullamco laboris nisi ut commodo consequat.</p>
  <p class="abs copy" style="left:685px;top:809px;width:404px">Duis aute irure dolor in reprehenderit in voluptate velit esse cillum dolore eu fugiat nulla pariatur. Excepteur sint occaecat cupidatat non proident, sunt in culpa qui officia deserunt mollit anim id est laborum.</p>
</section>

<section class="abs services">
  <div class="service-photo" style="left:111px;top:105px;background:linear-gradient(135deg,#e9ecef,#bfc4c8 60%,#8b9196)" role="img" aria-label="Painters on a ladder preparing paint in a bright interior"></div>
  <h3 class="service-title" style="left:655px;top:122px">Sed ut perspiciatis<br>unde omnis</h3>
  <p class="service-copy" style="left:657px;top:219px">Lorem ipsum dolor sit amet, consectetur adipiscing elit, sed do eiusmod tempor incididunt ut labore et dolore magna aliqua. Ut enim ad minim veniam, quis nostrud exercitation ullamco laboris nisi ut aliquip ex ea commodo consequat. Duis aute irure dolor in reprehenderit in voluptate velit esse cillum dolore eu fugiat nulla paria pteur sint occaecatea.</p>
  <a class="btn" style="left:657px;top:407px;width:138px;height:50px">Learn More</a>

  <h3 class="service-title" style="left:110px;top:573px">Sed ut perspiciatis<br>unde omnis</h3>
  <p class="service-copy" style="left:112px;top:670px">Lorem ipsum dolor sit amet, consectetur adipiscing elit, sed do eiusmod tempor incididunt ut labore et dolore magna aliqua. Ut enim ad minim veniam, quis nostrud exercitation ullamco laboris nisi ut aliquip ex ea commodo consequat. Duis aute irure dolor in reprehenderit in voluptate velit esse cillum dolore eu fugiat nulla paria pteur sint occaecatea.</p>
  <a class="btn" style="left:112px;top:858px;width:138px;height:50px">Learn More</a>
  <div class="service-photo" style="left:600px;top:556px;background:linear-gradient(160deg,#f1f2f2,#cfd3d4 55%,#8f9aa8)" role="img" aria-label="Worker in a safety vest painting a ceiling from a ladder"></div>

  <div class="service-photo" style="left:111px;top:1007px;background:linear-gradient(135deg,#f2f3f3,#dcdfe0 55%,#9ea7b0)" role="img" aria-label="Two painters rolling white paint onto a wall"></div>
  <h3 class="service-title" style="left:655px;top:1024px">Sed ut perspiciatis<br>unde omnis</h3>
  <p class="service-copy" style="left:657px;top:1121px">Lorem ipsum dolor sit amet, consectetur adipiscing elit, sed do eiusmod tempor incididunt ut labore et dolore magna aliqua. Ut enim ad minim veniam, quis nostrud exercitation ullamco laboris nisi ut aliquip ex ea commodo consequat. Duis aute irure dolor in reprehenderit in voluptate velit esse cillum dolore eu fugiat nulla paria pteur sint occaecatea.</p>
  <a class="btn" style="left:657px;top:1309px;width:138px;height:50px">Learn More</a>
</section>

<section>
  <blockquote class="abs quote">“Lorem ipsum dolor sit amet, consectetur adipiscing elit, sed do eiusmod tempor incididunt ut labore et dolore magna aliqua. Ut enim ad minim veniam, quis laborum.”</blockquote>
  <p class="abs quote-name">Dana Whitfield</p>
</section>

<div class="abs wide-photo" role="img" aria-label="Painters in a red boom lift working on a commercial building with blue glass windows"></div>

<section>
  <h2 class="abs heading contact-title">Get in Touch</h2>
  <p class="abs detail" style="left:111px;top:3438px;font-size:14.5px">Feel free to contact us with any questions</p>
  <p class="abs label" style="left:111px;top:3490px">Address:</p>
  <p class="abs detail" style="left:111px;top:3516px">218, Harbor Works Avenue, United States</p>
  <p class="abs label" style="left:111px;top:3561px">Email:</p>
  <p class="abs detail" style="left:111px;top:3587px">info@brushlinecoatings.com</p>
  <p class="abs label" style="left:111px;top:3633px">Phone:</p>
  <p class="abs detail" style="left:111px;top:3659px">+1 (555) 014 2290</p>

  <p class="abs form-label" style="left:531px;top:3381px">Name *</p>
  <div class="field" style="left:531px;top:3412px;width:275px;height:41px">First Name</div>
  <div class="field" style="left:814px;top:3412px;width:275px;height:41px">Last Name</div>
  <p class="abs form-label" style="left:531px;top:3470px">Email *</p>
  <div class="field" style="left:531px;top:3499px;width:558px;height:41px"></div>
  <p class="abs form-label" style="left:531px;top:3557px">Message *</p>
  <div class="field" style="left:531px;top:3585px;width:558px;height:95px"></div>
  <a class="btn" style="left:531px;top:3692px;width:138px;height:48px">Submit Now</a>
</section>

<footer class="abs footer">
  <div class="abs" style="left:111px;top:52px;display:flex;align-items:center;gap:12px">
    <span class="brand-dot"></span><span class="brand-name" style="line-height:40px">Brushline Coatings</span>
  </div>
  <p class="abs detail" style="left:111px;top:152px;font-size:14px;color:var(--ink)">218, Harbor Works Avenue, United States</p>
  <p class="abs" style="left:111px;top:206px;font-size:12px;color:var(--ink)">© 2023 Brushline Coatings &nbsp; / &nbsp; All Rights reserved</p>
  <p class="abs footer-head" style="left:759px;top:100px">ABOUT</p>
  <p class="abs footer-link" style="left:759px;top:142px">Blog<br>Contact Us</p>
  <p class="abs footer-head" style="left:990px;top:100px">COMPANY</p>
  <p class="abs footer-link" style="left:990px;top:142px">About Us<br>Services<br>Gallery</p>
</footer>

</body>
</html>
```